We need a business card design for our residential home building company based out of East Tennessee and the Smoky Mountains. We have 30 years of experience, and we plan to build homes not only in the state of Tennessee, but out of state as well. We are a different kind of production home builder; we aim to build homes cost-effectively and efficiently but with the character, dignity, and charm of historic homes. Our homes have a timeless style with modern floorplans and features. We would like to see designs that embody a classic style with accents of gold, red, and blue. The resulting business card should convey elegance, strength, character, and trust as well as the careful balance of the old and new.
Motto: "Handcrafting Your Heritage"
Target Market(s)
Adults 40+ from the Northern states looking to settle in Tennessee.
Industry/Entity Type
Residential
Contact Information for Business Card
Birchline Dwellworks, LLC
Marisol Thackett | Director of Operations
24815 Quarrybend Lane | Suite 500
Knoxville, TN 48261
Office: (555)314-2290
Mobile: (555)648-1173
Email: marisol@birchlinedwellworks.example

```html
<!DOCTYPE html>
<html lang="en">
<head>
<meta charset="utf-8">
<title>Birchline Dwellworks, LLC – Business Card</title>
<link rel="stylesheet" href="https://fonts.googleapis.com/css2?family=Old+Standard+TT:wght@400;700&family=PT+Sans:wght@400&display=swap">
<style>
  :root {
    --gold-deep: #a7793a;
    --gold-mid: #d8a74e;
    --gold-bright: #f5dc72;
    --bronze: #8c6a3c;
    --ink: #1e160d;
    --ink-soft: #2b2014;
    --edge-light: #fffbe6;
    --accent-red: #e0262b;
    --accent-white: #fbf7ee;
    --accent-blue: #3f7fd0;
  }
  html, body {
    margin: 0;
    padding: 0;
    width: 1200px;
    height: 699px;
    overflow: hidden;
    background: #ffffff;
  }
  .card {
    position: relative;
    width: 1200px;
    height: 699px;
    overflow: hidden;
    background: linear-gradient(180deg,
      var(--gold-deep) 0%,
      #c4924a 18%,
      var(--gold-mid) 35%,
      #e6bd5a 52%,
      var(--gold-bright) 64%,
      #f1d169 70%,
      #d3a24d 84%,
      var(--gold-deep) 100%);
  }
  .card::before {
    content: "";
    position: absolute;
    inset: 0;
    background: repeating-linear-gradient(180deg,
      rgba(255,255,255,0.05) 0 2px,
      rgba(0,0,0,0.03) 2px 5px);
  }
  .trim {
    position: absolute;
    left: 0;
    width: 1200px;
    height: 22px;
    background: linear-gradient(90deg,
      var(--edge-light) 0%, #e2c27c 6%, #8d6a33 14%, #e8cd88 24%,
      #b48a42 36%, var(--edge-light) 46%, #caa258 56%, #7d5c2a 66%,
      #f0d996 76%, #a57c3a 86%, var(--edge-light) 94%, #3d2e15 100%);
  }
  .trim--top { top: 0; }
  .trim--bottom { bottom: 0; }
  .brand-mark {
    position: absolute;
    left: 525px;
    top: 48px;
    width: 150px;
    height: 150px;
    border-radius: 50%;
    background: rgba(140, 106, 60, 0.35);
  }
  .brand-name {
    position: absolute;
    left: 0;
    right: 0;
    top: 226px;
    margin: 0;
    text-align: center;
    font-family: "PT Sans", sans-serif;
    font-weight: 400;
    font-size: 52px;
    line-height: 1;
    color: var(--bronze);
  }
  .motto {
    position: absolute;
    left: 0;
    right: 0;
    top: 292px;
    margin: 0;
    text-align: center;
    font-family: "PT Sans", sans-serif;
    font-size: 26px;
    line-height: 1;
    color: var(--ink-soft);
  }
  .accent-rule {
    position: absolute;
    left: 480px;
    top: 342px;
    width: 240px;
    height: 8px;
    display: flex;
  }
  .accent-rule span { flex: 1; }
  .accent-rule .red { background: var(--accent-red); }
  .accent-rule .white { background: var(--accent-white); }
  .accent-rule .blue { background: var(--accent-blue); }
  .line {
    position: absolute;
    left: 0;
    right: 0;
    margin: 0;
    text-align: center;
    line-height: 1;
    white-space: nowrap;
  }
  .line--name {
    top: 398px;
    font-family: "Old Standard TT", serif;
    font-weight: 700;
    font-size: 50px;
    color: var(--ink);
  }
  .line--detail {
    font-family: "PT Sans", sans-serif;
    font-size: 38px;
    color: var(--ink-soft);
  }
  .line--title { top: 466px; }
  .line--city { top: 520px; }
  .line--contact {
    font-family: "PT Sans", sans-serif;
    font-size: 46px;
    color: var(--ink-soft);
  }
  .line--phones { top: 566px; }
  .line--phones .gap { display: inline-block; width: 34px; }
  .line--email { top: 620px; }
</style>
</head>
<body>
  <div class="card">
    <div class="trim trim--top"></div>

    <div class="brand-mark"></div>
    <p class="brand-name">Birchline Dwellworks, LLC</p>
    <p class="motto">Handcrafting Your Heritage</p>
    <div class="accent-rule"><span class="red"></span><span class="white"></span><span class="blue"></span></div>

    <p class="line line--name">Birchline Dwellworks, LLC Marisol Thackett</p>
    <p class="line line--detail line--title">Director of Operations 24815 Quarrybend Lane</p>
    <p class="line line--detail line--city">Suite 500 Knoxville, TN 48261</p>
    <p class="line line--contact line--phones">Office: (555)314-2290<span class="gap"></span>Mobile: (555)648-1173</p>
    <p class="line line--contact line--email">Email: marisol@birchlinedwellworks.example</p>

    <div class="trim trim--bottom"></div>
  </div>
</body>
</html>
```